New Company Business Card Design

I have a new company logo and I want a new business card design. I dont know if the logo file i attached is in the correct format or quality. We are a New York City Specialty construction Firm specializing in high risk out of the box projects. I want a simple and classy business card that people will his card is as crisp as the work his company does.

Target Market(s)

Clients in the heavy construction industry in New York City

Industry/Entity Type

Construction Company

Contact Information for Business Card

Simple Classy - DIFFERENT

Font styles to use
Other font styles liked:
• Mach the logo font in some way

Colors

Designer to choose colors to be used in the design.

Requirements
Must have
• Uniqueness
Nice to have
• Nothing particular - Just different and classy - Timeless
Should not have
• Goofy Shit or Gimmicky shit

```html
<!DOCTYPE html>
<html lang="en">
<head>
<meta charset="utf-8">
<title>KRV Builders – Business Card</title>
<link href="https://fonts.googleapis.com/css2?family=Arimo:wght@400;700&display=swap" rel="stylesheet">
<style>
  :root {
    --bg: #2e2e2e;
    --blue-light: #1a9ad8;
    --blue-deep: #1c4f9c;
    --blue-text: #1a86cf;
    --ink: #111111;
    --paper: #ffffff;
  }
  * { margin: 0; padding: 0; box-sizing: border-box; }
  html, body {
    width: 1200px; height: 1200px; overflow: hidden;
    background: var(--bg);
    font-family: "Arimo", Arial, sans-serif;
  }
  .card {
    position: absolute; left: 160px;
    width: 880px; height: 503px;
    overflow: hidden;
    box-shadow: 0 10px 30px rgba(0,0,0,.45);
  }
  .card--front {
    top: 77px;
    background: linear-gradient(180deg, var(--blue-light) 0%, var(--blue-deep) 100%);
  }
  .card--back { top: 620px; background: var(--paper); }

  .brand {
    font-weight: 700; letter-spacing: 1px; line-height: 1;
    display: flex; align-items: center; white-space: nowrap;
  }
  .brand__mark { display: inline-block; flex: none; }

  .front__brand {
    position: absolute; top: 200px; left: 0; width: 100%;
    justify-content: center; gap: 14px;
    color: var(--paper); font-size: 56px;
  }
  .front__brand .brand__mark { width: 22px; height: 22px; background: var(--paper); }
  .front__web {
    position: absolute; top: 330px; left: 0; width: 100%;
    text-align: center; color: var(--paper);
    font-weight: 700; font-size: 19px; letter-spacing: 5px;
  }

  .back__brand {
    position: absolute; top: 176px; left: 46px; width: 370px;
    gap: 10px; color: var(--blue-text); font-size: 28px;
  }
  .back__brand .brand__mark { width: 18px; height: 18px; background: var(--blue-text); }
  .back__divider {
    position: absolute; left: 448px; top: 100px;
    width: 2px; height: 200px; background: var(--ink);
  }
  .contact { position: absolute; left: 482px; top: 104px; color: var(--ink); }
  .contact__name { font-weight: 700; font-size: 31px; line-height: 1; }
  .contact__title { color: var(--blue-text); font-size: 22px; margin-top: 2px; }
  .contact__address { font-size: 21px; line-height: 1.2; margin-top: 18px; }
  .contact__list { list-style: none; margin-top: 10px; font-size: 21px; line-height: 1.25; }
  .contact__list li { display: flex; align-items: center; gap: 10px; }
  .contact__list svg { width: 18px; height: 18px; fill: var(--blue-text); flex: none; }

  .back__wave { position: absolute; left: 0; top: 0; width: 880px; height: 503px; }
  .back__web {
    position: absolute; left: 540px; top: 458px;
    color: var(--paper); font-size: 24px; letter-spacing: 1px; line-height: 1;
  }
  .back__web span { color: var(--blue-light); }
</style>
</head>
<body>

<section class="card card--front">
  <div class="brand front__brand"><span class="brand__mark"></span>KRV BUILDERS, INC.</div>
  <div class="front__web">WWW.KRVBUILD.COM</div>
</section>

<section class="card card--back">
  <svg class="back__wave" viewBox="0 0 880 503" aria-hidden="true">
    <defs>
      <linearGradient id="swoosh" x1="0" x2="1" y1="0" y2="0">
        <stop offset="0" stop-color="#1c5aa8"/>
        <stop offset="1" stop-color="#1a9ad8"/>
      </linearGradient>
    </defs>
    <path d="M0 360 C 260 405, 600 400, 880 420 L880 503 L0 503 Z" fill="url(#swoosh)"/>
    <path d="M0 398 C 300 390, 610 395, 880 428 L880 503 L0 503 Z" fill="#ffffff"/>
    <path d="M0 404 C 300 396, 615 401, 880 434 L880 503 L0 503 Z" fill="url(#swoosh)"/>
    <path d="M0 412 C 300 404, 620 410, 880 442 L880 503 L0 503 Z" fill="#0d0d0d"/>
  </svg>

  <div class="brand back__brand"><span class="brand__mark"></span>KRV BUILDERS, INC.</div>
  <div class="back__divider"></div>

  <div class="contact">
    <div class="contact__name">Marco T. Bellini</div>
    <div class="contact__title">President &amp; CEO</div>
    <div class="contact__address">418 Harbor View Road<br>Linden, New Jersey 07036</div>
    <ul class="contact__list">
      <li><svg viewBox="0 0 24 24"><path d="M6.6 10.8a15.1 15.1 0 0 0 6.6 6.6l2.2-2.2c.3-.3.7-.4 1-.2 1.1.4 2.3.6 3.6.6.6 0 1 .4 1 1V20c0 .6-.4 1-1 1A17 17 0 0 1 3 4c0-.6.4-1 1-1h3.5c.6 0 1 .4 1 1 0 1.3.2 2.5.6 3.6.1.3 0 .7-.2 1z"/></svg>555-014-2210</li>
      <li><svg viewBox="0 0 24 24"><path d="M7 2h10a2 2 0 0 1 2 2v16a2 2 0 0 1-2 2H7a2 2 0 0 1-2-2V4a2 2 0 0 1 2-2zm0 3v13h10V5z"/></svg>555-018-3367</li>
      <li><svg viewBox="0 0 24 24"><path d="M2 5h20v14H2zm2 2v.5l8 5 8-5V7l-8 5z"/></svg>MARCO@KRVBUILD.COM</li>
    </ul>
  </div>

  <div class="back__web">www.<span>KRVBUILD</span>.COM</div>
</section>

</body>
</html>
```